Detail Shop Business card design

i need a business card design for my new detailing company called 'Brenner's Detail Shop'. i want an all black and white design . simple, direct and to the point. i want the designer to choose a fitting font to match the logothe front should have logo, address, phone and email and the back side should have a slogan and text indicating that we offer services on anything including cars, trucks, motorcycles and RVs. slogan will read "we take pride in your ride"
maybe also very small on the back side the IG icon with Brenners_Detail_Shop

phone 482.615.7734
address 7384 E Harlow Ave
Spokane WA 99342
email: BrennersDetail@quorvail.com

Target Market(s)

all ages , auto enthusiasts

Industry/Entity Type

Automotive

Contact Information for Business Card

the front should have logo, address, phone and email and the back side should have a slogan and text indicating that we offer services on anything including cars, trucks, motorcycles and RVs. slogan will read "we take pride in your ride"

phone 482.615.7734
address 7384 E Harlow Ave
Spokane WA 99342

Colors
000000
ffffff

Requirements
Must have
• bold font and very simple design with good spacing
Nice to have
• anything creative from the designer indicating we service any types of vehicles
Should not have
• any colors ,

```html
<!DOCTYPE html>
<html lang="en">
<head>
<meta charset="utf-8">
<title>Brenner's Detail Shop – Business Card</title>
<link rel="stylesheet" href="https://fonts.googleapis.com/css2?family=Roboto+Slab:wght@400;700&family=Noto+Serif:wght@400&family=Oswald:wght@400;500;600&display=swap">
<style>
  :root {
    --page: #e9e9e9;
    --paper: #ffffff;
    --ink: #111111;
    --ink-soft: #555555;
    --back-card: #555555;
    --back-ink: #141414;
    --art-light: #2e2e2e;
    --art-dark: #161616;
  }
  html, body {
    margin: 0;
    width: 1200px;
    height: 950px;
    overflow: hidden;
    background: var(--page);
  }
  .sheet {
    position: relative;
    width: 1200px;
    height: 950px;
  }
  .card {
    position: absolute;
    left: 250px;
    width: 700px;
    height: 400px;
    box-sizing: border-box;
    box-shadow: 0 6px 18px rgba(0,0,0,0.18);
    overflow: hidden;
  }
  .card--front { top: 40px; background: var(--paper); color: var(--ink); }
  .card--back  { top: 510px; background: var(--back-card); color: var(--back-ink); }

  /* front */
  .brand {
    position: absolute;
    right: 56px;
    top: 50px;
    display: flex;
    align-items: center;
    gap: 14px;
  }
  .brand__dot {
    width: 34px;
    height: 34px;
    border-radius: 50%;
    background: var(--ink);
  }
  .brand__name {
    margin: 0;
    font-family: "Roboto Slab", serif;
    font-weight: 700;
    font-size: 26px;
    color: var(--ink);
  }
  .person {
    position: absolute;
    left: 56px;
    top: 196px;
  }
  .person__name {
    margin: 0;
    font-family: "Roboto Slab", serif;
    font-weight: 700;
    font-size: 26px;
    line-height: 32px;
    letter-spacing: 0.5px;
    text-transform: uppercase;
  }
  .person__role {
    margin: 2px 0 0;
    font-family: "Roboto Slab", serif;
    font-weight: 700;
    font-size: 17px;
    color: var(--ink-soft);
    text-transform: uppercase;
  }
  .contact {
    position: absolute;
    left: 56px;
    top: 276px;
    margin: 0;
    padding: 0;
    list-style: none;
    font-family: "Noto Serif", serif;
    font-size: 16px;
    line-height: 29px;
    color: var(--ink-soft);
    white-space: nowrap;
  }
  .contact__label { margin-right: 6px; }
  .contact__label--mid { margin-left: 6px; }

  /* back */
  .vehicle-art {
    position: absolute;
    right: 60px;
    top: 36px;
    width: 460px;
    height: 190px;
    border-radius: 6px;
    background: radial-gradient(ellipse at 55% 50%, var(--art-light), var(--art-dark) 75%);
  }
  .tagline {
    position: absolute;
    left: 60px;
    top: 256px;
    margin: 0;
    padding-bottom: 8px;
    border-bottom: 2px solid var(--back-ink);
    font-family: "Oswald", sans-serif;
    font-weight: 600;
    font-size: 30px;
    line-height: 40px;
    letter-spacing: 1px;
    text-transform: uppercase;
  }
  .services {
    position: absolute;
    left: 60px;
    top: 320px;
    margin: 0;
    font-family: "Oswald", sans-serif;
    font-weight: 500;
    font-size: 19px;
    line-height: 26px;
  }
  .social {
    position: absolute;
    right: 60px;
    bottom: 22px;
    display: flex;
    align-items: center;
    gap: 7px;
    margin: 0;
    font-family: "Oswald", sans-serif;
    font-weight: 400;
    font-size: 13px;
  }
  .social__mark {
    width: 11px;
    height: 11px;
    background: var(--back-ink);
  }
</style>
</head>
<body>
<main class="sheet">
  <section class="card card--front" aria-label="Card front">
    <div class="brand">
      <span class="brand__dot"></span>
      <p class="brand__name">Brenner's Detail Shop</p>
    </div>
    <div class="person">
      <h1 class="person__name">Dale Morrow</h1>
      <p class="person__role">CEO/Founder</p>
    </div>
    <ul class="contact">
      <li><span class="contact__label">(A)</span>7384 E Harlow Ave, Spokane WA 99342</li>
      <li><span class="contact__label">(P)</span>482.615.7734<span class="contact__label contact__label--mid">(M)</span>417 592 3086</li>
      <li><span class="contact__label">(E)</span>BrennersDetail@quorvail.com<span class="contact__label contact__label--mid">(W)</span>www.brennersdetail.com</li>
    </ul>
  </section>

  <section class="card card--back" aria-label="Card back">
    <div class="vehicle-art" role="img" aria-label="Black silhouette illustration of a classic hot rod car in side view"></div>
    <h2 class="tagline">We take pride in your ride</h2>
    <p class="services">Services on anything including cars, trucks, motorcycles &amp; RVs</p>
    <p class="social"><span class="social__mark"></span>Brenners_Detail_Shop</p>
  </section>
</main>
</body>
</html>
```